MORIVO VEGAN SUSHI

www.morivo-restaurant.de
We are open in 2018 and are an innovative restaurant from Munich. We would like a cool design for our drinks and food menu. It's very simple at the moment. See the File menu. In any case, our logo should appear. On the website we use neutraface as a font. But it's not a must. We are only open in the evening and appeal to a young, upscale audience.

```html
<!DOCTYPE html>
<html lang="de">
<head>
<meta charset="utf-8">
<title>Morivo Vegan Sushi – Speisekarte</title>
<link href="https://fonts.googleapis.com/css2?family=Catamaran:wght@400;600;700&display=swap" rel="stylesheet">
<style>
  :root {
    --backdrop: #1f1c1a;
    --paper: #efedea;
    --ink: #1c1b1a;
    --ink-soft: #3a3837;
    --rule: #8b8885;
    --wave: #d9d6d2;
  }
  * { box-sizing: border-box; margin: 0; padding: 0; }
  html, body { width: 992px; height: 1200px; overflow: hidden; }
  body {
    background: var(--backdrop);
    font-family: "Catamaran", sans-serif;
    color: var(--ink);
    position: relative;
  }
  .menu-page {
    position: absolute;
    width: 405px;
    height: 525px;
    background: var(--paper);
    overflow: hidden;
  }
  .page-1 { left: 75px;  top: 64px; }
  .page-2 { left: 514px; top: 64px; }
  .page-3 { left: 75px;  top: 624px; }
  .page-4 { left: 516px; top: 623px; }

  .frame { position: absolute; inset: 0; pointer-events: none; }

  .brand-tab {
    position: absolute;
    left: 168px; top: 0;
    width: 68px; height: 98px;
    background: var(--ink);
    display: flex; align-items: flex-end; justify-content: center;
    padding-bottom: 16px;
  }
  .brand-name {
    color: var(--paper);
    font-weight: 600;
    font-size: 10px;
    letter-spacing: 2.4px;
  }

  .menu-content {
    position: absolute;
    left: 68px; width: 258px;
    top: 130px;
  }
  .page-4 .menu-content { left: 70px; }
  .menu-section { margin-bottom: 17px; }
  .menu-section.spacious { margin-bottom: 28px; }
  .section-head {
    display: flex; justify-content: space-between; align-items: baseline;
    border-bottom: 1px solid var(--rule);
    padding-bottom: 2px;
    margin-bottom: 6px;
  }
  .section-title {
    font-weight: 700;
    font-size: 12.5px;
    letter-spacing: 0.4px;
    line-height: 16px;
  }
  .section-note { font-size: 7px; color: var(--ink-soft); }
  .menu-item {
    display: flex; justify-content: space-between;
    font-size: 7.6px;
    line-height: 14.6px;
    color: var(--ink-soft);
  }
  .menu-item .price { white-space: nowrap; }
  .menu-item.two-line { line-height: 11.5px; padding: 1.5px 0 3px; }

  .wave-band {
    position: absolute;
    left: 0; right: 0; bottom: 0;
    height: 56px;
    background: linear-gradient(180deg, var(--paper) 0%, var(--wave) 35%, #cfcbc6 100%);
  }
  .allergy-note {
    position: absolute;
    left: 84px; top: 492px;
    width: 237px; height: 23px;
    background: var(--paper);
    border: 1px solid var(--ink-soft);
    display: flex; align-items: center;
    padding: 0 6px;
    gap: 6px;
  }
  .vegan-label {
    display: flex; align-items: center; gap: 6px;
    font-weight: 700; font-size: 9.5px; letter-spacing: 0.3px;
    padding-right: 8px;
    border-right: 1px solid var(--rule);
    height: 15px;
  }
  .allergy-text {
    font-size: 4.3px; line-height: 5.5px; color: var(--ink-soft);
  }
</style>
</head>
<body>

<!-- Page template repeated four times -->
<section class="menu-page page-1">
  <svg class="frame" width="405" height="525" viewBox="0 0 405 525">
    <g fill="none" stroke="#1c1b1a" stroke-width="1.2">
      <path d="M16 532 V28 L26 18 H164 M240 18 H378 L388 28 V532"/>
      <path d="M22 532 V32 M382 532 V32" stroke-width="0.7"/>
    </g>
  </svg>
  <div class="brand-tab"><span class="brand-name">MORIVO</span></div>
  <div class="menu-content">
    <div class="menu-section">
      <div class="section-head"><span class="section-title">CHEF MENÜ mit Aperitiv</span><span class="section-note">für 2 Personen</span></div>
      <div class="menu-item"><span>Kleine Portion Ramensuppe Mit Gemüse &amp; Nudeln</span><span class="price">81,00 €</span></div>
      <div class="menu-item"><span>Mini Set</span></div>
      <div class="menu-item"><span>Dessert</span></div>
    </div>
    <div class="menu-section">
      <div class="section-head"><span class="section-title">OMAKASE</span><span class="section-note">für 2 Personen</span></div>
      <div class="menu-item"><span>Edamame</span><span class="price">68,00 €</span></div>
      <div class="menu-item"><span>Omakase Set mit 8 Spezialitäten des Hauses</span></div>
      <div class="menu-item"><span>Pana Cotta Mit Beeren</span></div>
    </div>
    <div class="menu-section">
      <div class="section-head"><span class="section-title">SET 1</span></div>
      <div class="menu-item"><span>Hosomaki</span><span class="price">33,90 €</span></div>
      <div class="menu-item"><span>Futomaki</span></div>
      <div class="menu-item"><span>Nigiri</span></div>
      <div class="menu-item"><span>Kürbiskroketten</span></div>
      <div class="menu-item"><span>Wakame Gurken Salat</span></div>
      <div class="menu-item"><span>Pickles</span></div>
      <div class="menu-item"><span>Gyoza Teigtaschen</span></div>
      <div class="menu-item"><span>Sushi Cake</span></div>
    </div>
  </div>
  <div class="wave-band" role="img" aria-label="Japanisches Wellenmuster (Seigaiha) in Schwarz auf Weiß"></div>
  <div class="allergy-note">
    <span class="vegan-label"><svg width="13" height="10" viewBox="0 0 13 10"><path d="M6.5 9 C2 9 1 5 1.5 2 C4.5 2 6.5 4 6.5 9 Z M6.5 9 C11 9 12 5 11.5 2 C8.5 2 6.5 4 6.5 9 Z" fill="none" stroke="#1c1b1a" stroke-width="0.9"/></svg>ALL VEGAN</span>
    <span class="allergy-text">Bitte teilen Sie dem Service unbedingt Allergien mit und fragen Sie nach der Allergiker-Menükarte</span>
  </div>
</section>

<section class="menu-page page-2">
  <svg class="frame" width="405" height="525" viewBox="0 0 405 525">
    <g fill="none" stroke="#1c1b1a" stroke-width="1.2">
      <path d="M16 532 V28 L26 18 H164 M240 18 H378 L388 28 V532"/>
      <path d="M22 532 V32 M382 532 V32" stroke-width="0.7"/>
    </g>
  </svg>
  <div class="brand-tab"><span class="brand-name">MORIVO</span></div>
  <div class="menu-content">
    <div class="menu-section spacious">
      <div class="section-head"><span class="section-title">SET 2</span></div>
      <div class="menu-item"><span>Hosomaki</span><span class="price">31,90 €</span></div>
      <div class="menu-item"><span>Futomaki</span></div>
      <div class="menu-item"><span>Pickles</span></div>
      <div class="menu-item"><span>Sushi “Thuna” Cake</span></div>
      <div class="menu-item"><span>Crispy Auberginen mit Mayo</span></div>
      <div class="menu-item"><span>Aubergine Dengaku</span></div>
    </div>
    <div class="menu-section">
      <div class="section-head"><span class="section-title">SET 3</span></div>
      <div class="menu-item"><span>Hosomaki</span><span class="price">28,90 €</span></div>
      <div class="menu-item"><span>Uramaki</span></div>
      <div class="menu-item"><span>Nigiri</span></div>
      <div class="menu-item"><span>Gemüse Tempura</span></div>
      <div class="menu-item"><span>Crispy Tofusticks mit Mayo</span></div>
      <div class="menu-item"><span>Wakame Shira Ae</span></div>
    </div>
  </div>
  <div class="wave-band" role="img" aria-label="Japanisches Wellenmuster (Seigaiha) in Schwarz auf Weiß"></div>
  <div class="allergy-note">
    <span class="vegan-label"><svg width="13" height="10" viewBox="0 0 13 10"><path d="M6.5 9 C2 9 1 5 1.5 2 C4.5 2 6.5 4 6.5 9 Z M6.5 9 C11 9 12 5 11.5 2 C8.5 2 6.5 4 6.5 9 Z" fill="none" stroke="#1c1b1a" stroke-width="0.9"/></svg>ALL VEGAN</span>
    <span class="allergy-text">Bitte teilen Sie dem Service unbedingt Allergien mit und fragen Sie nach der Allergiker-Menükarte</span>
  </div>
</section>

<section class="menu-page page-3">
  <svg class="frame" width="405" height="525" viewBox="0 0 405 525">
    <g fill="none" stroke="#1c1b1a" stroke-width="1.2">
      <path d="M16 532 V28 L26 18 H164 M240 18 H378 L388 28 V532"/>
      <path d="M22 532 V32 M382 532 V32" stroke-width="0.7"/>
    </g>
  </svg>
  <div class="brand-tab"><span class="brand-name">MORIVO</span></div>
  <div class="menu-content">
    <div class="menu-section">
      <div class="section-head"><span class="section-title">VORSPEISEN</span></div>
      <div class="menu-item"><span>Miso Suppe</span><span class="price">5,50 €</span></div>
      <div class="menu-item"><span>Edamame Mit Salz/chili</span><span class="price">4,50 €</span></div>
      <div class="menu-item"><span>Seidentofu in hausgemachter Sauce mit Mandeln</span><span class="price">5,50 €</span></div>
    </div>
    <div class="menu-section">
      <div class="section-head"><span class="section-title">SUSHI</span></div>
      <div class="menu-item"><span>Uramaki mit Tempuragemüse</span><span class="price">8,90 €</span></div>
      <div class="menu-item"><span>Futomaki wechselndes Gemüse</span><span class="price">8,00 €</span></div>
      <div class="menu-item"><span>Uramaki mit Austernpilze</span><span class="price">7,50 €</span></div>
      <div class="menu-item"><span>Hosomaki Gurke Avocado</span><span class="price">5,50 €</span></div>
      <div class="menu-item"><span>Hosomaki Gurke Shiitake</span><span class="price">5,50 €</span></div>
      <div class="menu-item"><span>Tomaten Nigiri</span><span class="price">4,50 €</span></div>
    </div>
    <div class="menu-section">
      <div class="section-head"><span class="section-title">KLEINE GERICHTE</span></div>
      <div class="menu-item"><span>Gemüse Tempura</span><span class="price">8,00 €</span></div>
      <div class="menu-item"><span>Crispy Tofusticks mit Mayo</span><span class="price">8,00 €</span></div>
      <div class="menu-item"><span>Kürbiskroketten mit Tangashu</span><span class="price">7,90 €</span></div>
      <div class="menu-item"><span>Sushi “Thuna” Cake</span><span class="price">6,90 €</span></div>
      <div class="menu-item"><span>Sushi Cake Classic</span><span class="price">6,00 €</span></div>
      <div class="menu-item"><span>Aubergine Dengaku</span><span class="price">5,50 €</span></div>
    </div>
  </div>
  <div class="wave-band" role="img" aria-label="Japanisches Wellenmuster (Seigaiha) in Schwarz auf Weiß"></div>
  <div class="allergy-note">
    <span class="vegan-label"><svg width="13" height="10" viewBox="0 0 13 10"><path d="M6.5 9 C2 9 1 5 1.5 2 C4.5 2 6.5 4 6.5 9 Z M6.5 9 C11 9 12 5 11.5 2 C8.5 2 6.5 4 6.5 9 Z" fill="none" stroke="#1c1b1a" stroke-width="0.9"/></svg>ALL VEGAN</span>
    <span class="allergy-text">Bitte teilen Sie dem Service unbedingt Allergien mit und fragen Sie nach der Allergiker-Menükarte</span>
  </div>
</section>

<section class="menu-page page-4">
  <svg class="frame" width="405" height="525" viewBox="0 0 405 525">
    <g fill="none" stroke="#1c1b1a" stroke-width="1.2">
      <path d="M16 532 V28 L26 18 H164 M240 18 H378 L388 28 V532"/>
      <path d="M22 532 V32 M382 532 V32" stroke-width="0.7"/>
    </g>
  </svg>
  <div class="brand-tab"><span class="brand-name">MORIVO</span></div>
  <div class="menu-content">
    <div class="menu-section spacious">
      <div class="section-head"><span class="section-title">HAUPTSPEISEN</span></div>
      <div class="menu-item two-line"><span>Herrlich cremiges Katsu Curry<br>mit knusprigen Auberginensticks, Reis &amp; Pickles</span><span class="price">17,90 €</span></div>
      <div class="menu-item"><span>Ramen Suppe mit Nudeln, Gemüse &amp; Tofu</span><span class="price">14,90 €</span></div>
      <div class="menu-item"><span>Chirashi Sushi Bowl</span><span class="price">13,90 €</span></div>
      <div class="menu-item"><span>Sommersalate mit Sesamdressing &amp; Crispy Tofusticks mit Mayo</span><span class="price">12,50 €</span></div>
    </div>
    <div class="menu-section">
      <div class="section-head"><span class="section-title">DESSERT</span></div>
      <div class="menu-item"><span>Cheesecake mit Beeren</span><span class="price">6,50 €</span></div>
      <div class="menu-item"><span>Pana Cotta mit Beeren</span><span class="price">5,90 €</span></div>
      <div class="menu-item"><span>Sorbet des Tages</span><span class="price">5,50 €</span></div>
      <div class="menu-item"><span>Sorbet des Tages mit Schuss</span><span class="price">6,90 €</span></div>
    </div>
  </div>
  <div class="wave-band" role="img" aria-label="Japanisches Wellenmuster (Seigaiha) in Schwarz auf Weiß"></div>
  <div class="allergy-note">
    <span class="vegan-label"><svg width="13" height="10" viewBox="0 0 13 10"><path d="M6.5 9 C2 9 1 5 1.5 2 C4.5 2 6.5 4 6.5 9 Z M6.5 9 C11 9 12 5 11.5 2 C8.5 2 6.5 4 6.5 9 Z" fill="none" stroke="#1c1b1a" stroke-width="0.9"/></svg>ALL VEGAN</span>
    <span class="allergy-text">Bitte teilen Sie dem Service unbedingt Allergien mit und fragen Sie nach der Allergiker-Menükarte</span>
  </div>
</section>

</body>
</html>
```